IT Tradingsystem for car dealers needs Business Card Design

We need a fresh and modern design for our new business cards.

We develop a it-business system for car dealers in Sweden, Norway and on our way down to further countries in Europe, hence the namechange to BrolaTek Europe AB. The site can be found at www.brolatek-example.com. The startpage is also in for an update/modernization soon so don't take to much from here.

We are looking to print double sided, 4-colour cards.

We want to look professional, modern and serious. Open to cooler suggestions, but not too crazy. We need to make a good and serious impression on our potential customers. It needs to reflect our scandinavian design values and layout.

Preferably with the full BrolaTek logo in good size on the back, so the small print on the logo can be read easily.

Text that needs to go on the cards:
-------

Per Oskar Fjellström
Founder

Direct +46 70-512 96 47
Support 08-612 57 394
po.fjellstrom@brolatek-example.com

BrolaTek Europe AB
Box 8617
104 29 Stockholm

Brolatek-example.com
Saljportalen-example.se

--------
Good luck and thanks!

PS. If you need more input or see what our previous cards looked like, don't hesitate to contact me!

Target Market(s)

Decision makers / executives at brand cardealers

Industry/Entity Type

Automotive

Contact Information for Business Card

Normal size

Requirements
Must have
• Full logo
Nice to have
• Base on our orange colors
Should not have
• No fonts with serif, and not too much graphics

```html
<!DOCTYPE html>
<html lang="sv">
<head>
<meta charset="utf-8">
<title>BrolaTek – Business Card</title>
<link href="https://fonts.googleapis.com/css2?family=Arimo:wght@400;700&family=Open+Sans:wght@400&display=swap" rel="stylesheet">
<style>
  :root {
    --bg: #e3e3e3;
    --card: #ffffff;
    --orange: #e87722;
    --orange-light: #f2a15a;
    --ink: #1f1d1e;
    --text: #454545;
  }
  * { margin: 0; padding: 0; box-sizing: border-box; }
  html, body { width: 1200px; height: 1000px; overflow: hidden; background: var(--bg); }
  .stage { position: relative; width: 1200px; height: 1000px; }
  .card {
    position: absolute; top: 332px; width: 557px; height: 312px;
    background: var(--card); border-radius: 14px; overflow: hidden;
  }
  .card--front { left: 26px; }
  .card--back { left: 611px; }

  .brand { position: absolute; display: flex; align-items: center; }
  .brand__mark { background: var(--orange); flex: none; }
  .brand__name { font-family: "Arimo", Arial, sans-serif; font-weight: 700; color: var(--ink); letter-spacing: -0.5px; line-height: 1; }
  .brand__tagline { font-family: "Arimo", Arial, sans-serif; color: var(--ink); line-height: 1; margin-top: 4px; }

  .card--front .brand { left: 14px; top: 26px; }
  .card--front .brand__mark { width: 50px; height: 50px; margin-right: 20px; }
  .card--front .brand__name { font-size: 40px; }
  .card--front .brand__tagline { font-size: 12.5px; padding-left: 2px; }

  .card--back .brand { left: 277px; top: 246px; }
  .card--back .brand__mark { width: 42px; height: 42px; margin-right: 14px; }
  .card--back .brand__name { font-size: 32px; }
  .card--back .brand__tagline { font-size: 10px; padding-left: 1px; }

  .person { position: absolute; left: 23px; top: 143px; font-family: "Arimo", Arial, sans-serif; }
  .person__name { font-size: 18.5px; font-weight: 700; color: var(--orange); text-transform: uppercase; }
  .person__role { font-size: 12px; color: var(--ink); margin-top: 3px; text-transform: uppercase; }

  .contact { position: absolute; left: 22px; top: 196px; list-style: none; font-family: "Open Sans", Arial, sans-serif; font-size: 14px; color: var(--text); }
  .contact__item { display: flex; align-items: flex-start; height: 22px; }
  .contact__item--address { margin-top: 6px; line-height: 17px; height: auto; }
  .contact__icon { width: 14px; height: 14px; margin: 2px 15px 0 0; flex: none; }

  .accent { position: absolute; top: 0; height: 312px; background: var(--orange); }
  .card--front .accent { left: 417px; width: 140px; }
  .card--back .accent { left: 0; width: 146px; }
</style>
</head>
<body>
<main class="stage">
  <section class="card card--front" aria-label="Front of business card">
    <div class="brand">
      <span class="brand__mark"></span>
      <div>
        <div class="brand__name">BrolaTek</div>
        <div class="brand__tagline">BrukTest | Remarketing | saljportalen-example.se</div>
      </div>
    </div>

    <div class="person">
      <div class="person__name">Per Oskar Fjellström</div>
      <div class="person__role">Founder</div>
    </div>

    <ul class="contact">
      <li class="contact__item">
        <svg class="contact__icon" viewBox="0 0 14 14" fill="none" stroke="var(--orange)" stroke-width="1.1"><path d="M3 1.5l2 2.5-1.2 1.5c.8 1.8 2 3 3.7 3.7L9 8l2.5 2-1 2c-4.5-.3-8.3-4.1-8.5-8.5z"/></svg>
        +46 70-512 96 47
      </li>
      <li class="contact__item">
        <svg class="contact__icon" viewBox="0 0 14 14" fill="none" stroke="var(--orange)" stroke-width="1.1"><rect x="1" y="3" width="12" height="8.5"/><path d="M1 3l6 5 6-5"/></svg>
        po.fjellstrom@brolatek-example.com
      </li>
      <li class="contact__item">
        <svg class="contact__icon" viewBox="0 0 14 14" fill="none" stroke="var(--orange)" stroke-width="1.1"><circle cx="7" cy="7" r="6"/><ellipse cx="7" cy="7" rx="2.6" ry="6"/><path d="M1 7h12"/></svg>
        brolatek-example.com | saljportalen-example.se
      </li>
      <li class="contact__item contact__item--address">
        <svg class="contact__icon" viewBox="0 0 14 14" fill="none" stroke="var(--orange)" stroke-width="1.1"><path d="M7 13s4.5-4.5 4.5-7.5a4.5 4.5 0 0 0-9 0C2.5 8.5 7 13 7 13z"/><circle cx="7" cy="5.5" r="1.6"/></svg>
        <span>BrolaTek Europe AB Box 8617<br>104 29 Stockholm</span>
      </li>
    </ul>

    <div class="accent"></div>
  </section>

  <section class="card card--back" aria-label="Back of business card">
    <div class="accent"></div>
    <div class="brand">
      <span class="brand__mark"></span>
      <div>
        <div class="brand__name">BrolaTek</div>
        <div class="brand__tagline">BrukTest | Remarketing | saljportalen-example.se</div>
      </div>
    </div>
  </section>
</main>
</body>
</html>
```